Fresh-Up our Master Presentation

We are looking for someone who can revise our main presentation and make it more attractive. The previous layout and the slides are uploaded here and need to be revised. You are welcome to work with icons etc. here. The goal is to make it look a little more creative and modern. Brisk Otter is a company from the creative industry and therefore it would be great if it also shows this.

Target Market(s)

B2B

Industry/Entity Type

Communication and Content Creation

Font styles to use
Sans Serif

```html
<!DOCTYPE html>
<html lang="de">
<head>
<meta charset="utf-8">
<title>Brisk Otter – Master Presentation</title>
<link rel="stylesheet" href="https://fonts.googleapis.com/css2?family=Montserrat:wght@400;500;600;700;800&display=swap">
<style>
  :root{
    --navy:#2b3850;
    --navy-deep:#1f2a3d;
    --accent:#e4572e;
    --paper:#ffffff;
    --canvas:#eef0f3;
    --muted:#7d8799;
    --chip:#eef1f5;
    --photo-office-a:#4f6787;
    --photo-office-b:#b9c6d6;
    --photo-warm-a:#8a7a6c;
    --photo-warm-b:#d8d2ca;
    --photo-stage-a:#2a2f6b;
    --photo-stage-b:#7b5cc4;
    --photo-city-a:#3c4a5e;
    --photo-city-b:#aeb9c7;
  }
  *{box-sizing:border-box;margin:0;padding:0}
  html,body{width:814px;height:1200px;overflow:hidden}
  body{background:var(--canvas);font-family:"Montserrat",sans-serif;color:var(--navy)}
  .canvas{position:relative;width:814px;height:1200px;overflow:hidden}

  .sheet-brand{position:absolute;top:30px;right:34px;display:flex;align-items:center;gap:8px;font-size:18px;font-weight:700;color:var(--navy)}
  .mark{display:inline-block;width:14px;height:14px;border-radius:50%;background:currentColor}
  .mark--small{width:9px;height:9px}

  .slide{position:absolute;width:373px;height:210px;overflow:hidden;background:var(--paper);box-shadow:0 3px 12px rgba(31,42,61,.16)}
  .slide--hero{left:146px;top:110px;transform:scale(1.4);transform-origin:top left;box-shadow:0 6px 18px rgba(31,42,61,.14)}
  .slide--r1a{left:22px;top:495px}
  .slide--r1b{left:419px;top:495px}
  .slide--r2a{left:22px;top:715px}
  .slide--r2b{left:419px;top:715px}
  .slide--r3a{left:22px;top:935px}
  .slide--r3b{left:419px;top:935px}

  .slide--dark{background:var(--navy)}
  .brand{position:absolute;display:flex;align-items:center;gap:5px;font-size:11px;font-weight:700;color:var(--navy)}
  .slide--dark .brand,.contact-panel .brand{color:var(--paper)}

  .photo{position:absolute}
  .photo--office{background:linear-gradient(135deg,var(--photo-office-a),var(--photo-office-b))}
  .photo--warm{background:linear-gradient(160deg,var(--photo-warm-b),var(--photo-warm-a))}
  .photo--stage{background:radial-gradient(circle at 50% 30%,var(--photo-stage-b),var(--photo-stage-a) 70%)}
  .photo--city{background:linear-gradient(180deg,var(--photo-city-b),var(--photo-city-a))}

  .title-photo{right:0;top:0;width:190px;height:194px;clip-path:polygon(28% 0,100% 0,100% 100%,0 100%)}
  .title{position:absolute;left:18px;top:64px;font-size:19px;line-height:1.12;font-weight:800;color:var(--navy)}
  .slide--dark .title{color:var(--paper)}
  .rule{position:absolute;width:28px;height:3px;background:var(--accent)}
  .subtitle{position:absolute;left:18px;top:126px;font-size:6.5px;font-weight:500;color:var(--muted)}
  .slide--dark .subtitle{color:#c8d0dc}
  .date{position:absolute;left:18px;top:154px;font-size:4.8px;color:var(--muted)}
  .slide--dark .date{color:#aab4c3}
  .footer{position:absolute;left:0;right:0;bottom:0;height:16px;background:var(--paper);font-size:4.5px;color:var(--muted);display:flex;align-items:center;justify-content:center}

  .heading{position:absolute;font-size:13px;line-height:1.15;font-weight:800;color:var(--navy)}
  .bullets{position:absolute;list-style:none;font-size:5.2px;line-height:1.45;color:#4a556a}
  .bullets li{position:relative;padding-left:9px;margin-bottom:4px}
  .bullets li::before{content:"";position:absolute;left:0;top:2px;width:4px;height:4px;background:var(--navy)}

  .social-band{position:absolute;left:0;top:0;right:0;height:36px;background:var(--navy)}
  .social-band .heading{left:16px;top:11px;color:var(--paper);font-size:12px}
  .person{position:absolute;top:44px;width:170px}
  .person__name{font-size:7.5px;font-weight:700;color:var(--navy);margin-bottom:5px}
  .phone{position:absolute;top:14px;left:0;width:48px;height:94px;border-radius:8px;border:3px solid var(--navy-deep);overflow:hidden}
  .phone .photo{inset:0}
  .handles{position:absolute;top:18px;left:56px;list-style:none}
  .handles li{display:flex;align-items:center;gap:4px;width:100px;height:15px;margin-bottom:4px;padding:0 5px;background:var(--chip);font-size:5px;color:var(--navy);white-space:nowrap}
  .handles li::before{content:"";flex:none;width:6px;height:6px;border-radius:50%;background:var(--navy)}

  .icon-list{position:absolute;list-style:none;font-size:5.2px;line-height:1.4;color:#4a556a}
  .icon-list li{display:flex;align-items:flex-start;gap:6px;margin-bottom:7px;width:150px}
  .icon-list svg{flex:none}

  .contact-panel{position:absolute;left:0;top:0;bottom:0;width:190px;background:var(--navy)}
  .avatar{position:absolute;left:20px;top:20px;width:46px;height:46px;border-radius:50%;border:2px solid var(--paper)}
  .tagline{position:absolute;left:20px;top:98px;font-size:5.2px;color:#c8d0dc}
  .contact-list{position:absolute;left:20px;top:118px;list-style:none;font-size:5.5px;color:var(--paper)}
  .contact-list li{display:flex;align-items:center;gap:6px;margin-bottom:7px}
</style>
</head>
<body>
<div class="canvas">

  <div class="sheet-brand"><span class="mark"></span>Brisk Otter</div>

  <section class="slide slide--dark slide--hero">
    <div class="brand" style="left:18px;top:16px"><span class="mark mark--small"></span>Brisk Otter</div>
    <div class="photo photo--office title-photo" role="img" aria-label="Photo of a team working together in a modern office"></div>
    <h1 class="title">Presentation<br>Title Goes Here</h1>
    <div class="rule" style="left:18px;top:116px"></div>
    <p class="subtitle">Sub Title of Presentation Goes Here</p>
    <p class="date">Friday, May 10, 2024</p>
    <div class="footer">Master Deck 2024</div>
  </section>

  <section class="slide slide--dark slide--r1a">
    <div class="brand" style="left:18px;top:16px"><span class="mark mark--small"></span>Brisk Otter</div>
    <div class="photo photo--office title-photo" role="img" aria-label="Photo of a team working together in a modern office"></div>
    <h2 class="title">Presentation<br>Title Goes Here</h2>
    <div class="rule" style="left:18px;top:116px"></div>
    <p class="subtitle">Sub Title of Presentation Goes Here</p>
    <p class="date">Friday, May 10, 2024</p>
    <div class="footer">Master Deck 2024</div>
  </section>

  <section class="slide slide--r1b">
    <div class="brand" style="left:18px;top:16px"><span class="mark mark--small"></span>Brisk Otter</div>
    <div class="photo photo--office title-photo" role="img" aria-label="Photo of a team working together in a modern office"></div>
    <h2 class="title">Presentation<br>Title Goes Here</h2>
    <div class="rule" style="left:18px;top:116px"></div>
    <p class="subtitle">Sub Title of Presentation Goes Here</p>
    <p class="date">Friday, May 10, 2024</p>
    <div class="footer" style="background:var(--chip)">Master Deck 2024</div>
  </section>

  <section class="slide slide--r2a">
    <div class="photo photo--warm" style="left:0;top:0;width:152px;height:178px" role="img" aria-label="Portrait photo of the two founders"></div>
    <div class="brand" style="left:14px;top:188px;font-size:9px"><span class="mark mark--small"></span>Brisk Otter</div>
    <h2 class="heading" style="left:168px;top:24px">Jonas Keller und<br>Lukas Brandt</h2>
    <div class="rule" style="left:168px;top:60px"></div>
    <ul class="bullets" style="left:168px;top:72px;width:185px">
      <li>Gründer und kreative Köpfe hinter allen Projekten seit vielen Jahren.</li>
      <li>Spezialisiert auf Content, Kampagnen und Markenkommunikation.</li>
      <li>Über zehn Jahre Erfahrung mit Kunden aus ganz Europa.</li>
      <li>Gemeinsam mit dem Team entstehen Ideen, die wirken.</li>
    </ul>
    <div class="footer" style="left:auto;width:160px;right:0;background:transparent">Master Deck 2024</div>
  </section>

  <section class="slide slide--r2b">
    <div class="social-band"><h2 class="heading">Social Media-Präsenz</h2></div>
    <div class="person" style="left:14px">
      <p class="person__name">Jonas Keller</p>
      <div class="phone"><div class="photo photo--warm" role="img" aria-label="Social media profile photo of Jonas Keller"></div></div>
      <ul class="handles"><li>Foto-Kanal · 12k Follower</li><li>Business-Profil · 4k</li><li>Video-Kanal · 8k Abos</li><li>Kurzvideos · 20k Follower</li></ul>
    </div>
    <div class="person" style="left:194px">
      <p class="person__name">Lukas Brandt</p>
      <div class="phone"><div class="photo photo--warm" role="img" aria-label="Social media profile photo of Lukas Brandt"></div></div>
      <ul class="handles"><li>Foto-Kanal · 9k Follower</li><li>Business-Profil · 3k</li><li>Video-Kanal · 6k Abos</li><li>Kurzvideos · 15k Follower</li></ul>
    </div>
  </section>

  <section class="slide slide--r3a">
    <h2 class="heading" style="left:16px;top:20px">Der Podcast</h2>
    <div class="rule" style="left:16px;top:40px"></div>
    <ul class="icon-list" style="left:16px;top:56px">
      <li><svg width="9" height="9" viewBox="0 0 10 10"><circle cx="5" cy="5" r="5" fill="#2b3850"/><path d="M3 5.2l1.4 1.4L7.2 3.8" stroke="#fff" stroke-width="1.2" fill="none"/></svg>Wöchentliche Folgen rund um Kreativität und Content.</li>
      <li><svg width="9" height="9" viewBox="0 0 10 10"><circle cx="5" cy="5" r="5" fill="#2b3850"/><path d="M3 5.2l1.4 1.4L7.2 3.8" stroke="#fff" stroke-width="1.2" fill="none"/></svg>Spannende Gäste aus Marketing, Medien und Kultur.</li>
      <li><svg width="9" height="9" viewBox="0 0 10 10"><circle cx="5" cy="5" r="5" fill="#2b3850"/><path d="M3 5.2l1.4 1.4L7.2 3.8" stroke="#fff" stroke-width="1.2" fill="none"/></svg>Live-Aufnahmen vor Publikum auf großen Bühnen.</li>
      <li><svg width="9" height="9" viewBox="0 0 10 10"><circle cx="5" cy="5" r="5" fill="#2b3850"/><path d="M3 5.2l1.4 1.4L7.2 3.8" stroke="#fff" stroke-width="1.2" fill="none"/></svg>Verfügbar auf allen gängigen Plattformen.</li>
    </ul>
    <div class="photo photo--stage" style="left:190px;top:28px;width:165px;height:136px" role="img" aria-label="Photo of a live podcast recording on a lit stage"></div>
    <div class="footer">Master Deck 2024</div>
  </section>

  <section class="slide slide--r3b">
    <div class="contact-panel">
      <div class="photo photo--warm avatar" role="img" aria-label="Round portrait photo of the contact person"></div>
      <div class="brand" style="left:20px;top:76px"><span class="mark mark--small"></span>Brisk Otter</div>
      <p class="tagline">Mit Feuer dabei in der Zusammenarbeit</p>
      <ul class="contact-list">
        <li><svg width="8" height="8" viewBox="0 0 10 10"><path d="M2 1h2l1 2.5-1.2 1a6 6 0 0 0 2.7 2.7l1-1.2L10 7v2a1 1 0 0 1-1 1A8 8 0 0 1 1 2a1 1 0 0 1 1-1z" fill="#fff"/></svg>+41 44 555 01 23</li>
        <li><svg width="8" height="8" viewBox="0 0 10 10"><rect x="0.5" y="2" width="9" height="6" fill="none" stroke="#fff"/><path d="M0.5 2L5 5.5 9.5 2" fill="none" stroke="#fff"/></svg>hello@briskotter.example</li>
        <li><svg width="8" height="8" viewBox="0 0 10 10"><circle cx="5" cy="5" r="4.3" fill="none" stroke="#fff"/><path d="M0.7 5h8.6M5 0.7c-2.4 2.4-2.4 6.2 0 8.6M5 0.7c2.4 2.4 2.4 6.2 0 8.6" fill="none" stroke="#fff" stroke-width=".8"/></svg>www.briskotter.example</li>
      </ul>
    </div>
    <div class="photo photo--city" style="left:190px;top:0;right:0;bottom:0" role="img" aria-label="Photo looking up at modern office towers"></div>
  </section>

</div>
</body>
</html>
```